Kneadwell Haven Business Card Design

I want to create a very elegant and sophisticated two sided business card for my massage practice (www.kneadwellhaven-example.com). I have attached the logo and a PDF with some ideas down for the back of the card but I am open to suggestions. I will want to tie in a post card and flyer to the card later.
Similar colors to website would be great.
Target Market(s)
High end clientele, people looking for a sophisticated spa experience.
Industry/Entity Type
Massage
Contact Information for Business Card
Kneadwell Haven
7218 Larchmont Blvd S, Suite 305
Seattle, WA 98103
(555) 340-7816
www.kneadwellhaven-example.com

```html
<!DOCTYPE html>
<html lang="en">
<head>
<meta charset="utf-8">
<title>Kneadwell Haven Business Card</title>
<link href="https://fonts.googleapis.com/css2?family=Cinzel:wght@500&family=PT+Sans:wght@400&display=swap" rel="stylesheet">
<style>
  :root {
    --backdrop: #161616;
    --card-white: #ffffff;
    --ink-navy: #1d3443;
    --ink-text: #2a2a2a;
    --rule-grey: #9aa3a8;
    --back-teal: #1c2f3b;
    --back-pattern: #24394a;
    --logo-white: #ffffff;
  }
  * { margin: 0; padding: 0; box-sizing: border-box; }
  html, body {
    width: 1200px; height: 900px; overflow: hidden;
    background: var(--backdrop);
  }
  .stage { position: relative; width: 1200px; height: 900px; }
  .card {
    position: absolute; top: 306px; height: 271px;
  }
  .card-front { left: 149px; width: 439px; background: var(--card-white); }
  .card-back { left: 608px; width: 441px; background: var(--back-teal); }

  .brand-mark {
    position: absolute; left: 20px; top: 118px; width: 180px;
    text-align: center;
    font-family: "Cinzel", serif; font-weight: 500;
    font-size: 15px; letter-spacing: 0.5px;
    color: var(--ink-navy);
  }
  .divider {
    position: absolute; left: 212px; top: 72px; width: 1px; height: 126px;
    background: var(--rule-grey);
  }
  .details {
    position: absolute; left: 233px; top: 72px;
    font-family: "PT Sans", sans-serif; color: var(--ink-text);
  }
  .person-name, .company-name {
    font-family: "Cinzel", serif; font-weight: 500;
    font-size: 16px; color: var(--ink-navy); letter-spacing: 0.4px;
    line-height: 18px;
  }
  .person-role { font-size: 13px; line-height: 16px; margin-bottom: 5px; }
  .contact-line { font-size: 13px; line-height: 17px; display: flex; align-items: center; gap: 3px; }
  .contact-line svg { width: 10px; height: 10px; fill: var(--ink-text); }
  .company-name { margin-top: 7px; }
  .address { font-size: 13px; line-height: 16px; }

  .back-pattern {
    position: absolute; inset: 0;
    background: radial-gradient(circle at center, var(--back-pattern) 0%, var(--back-teal) 70%);
  }
  .back-mark {
    position: absolute; left: 0; right: 0; top: 94px;
    text-align: center;
    font-family: "Cinzel", serif; font-weight: 500;
    font-size: 11px; letter-spacing: 0.3px;
    color: var(--logo-white);
  }
</style>
</head>
<body>
<div class="stage">
  <section class="card card-front">
    <div class="brand-mark">KNEADWELL HAVEN</div>
    <div class="divider"></div>
    <div class="details">
      <div class="person-name">DANIEL HARPER</div>
      <div class="person-role">Managing Director</div>
      <div class="contact-line">
        <svg viewBox="0 0 24 24" aria-hidden="true"><path d="M6.6 10.8a15.1 15.1 0 0 0 6.6 6.6l2.2-2.2a1 1 0 0 1 1-.25 11.4 11.4 0 0 0 3.6.57 1 1 0 0 1 1 1V20a1 1 0 0 1-1 1A17 17 0 0 1 3 4a1 1 0 0 1 1-1h3.5a1 1 0 0 1 1 1c0 1.25.2 2.45.57 3.57a1 1 0 0 1-.25 1z"/></svg>
        <span>(555) 340-7816</span>
      </div>
      <div class="contact-line">
        <svg viewBox="0 0 24 24" aria-hidden="true"><circle cx="12" cy="12" r="11"/></svg>
        <span>www.kneadwellhaven-example.com</span>
      </div>
      <div class="company-name">KNEADWELL HAVEN</div>
      <div class="address">7218 Larchmont Blvd S, Suite 305</div>
      <div class="address">Seattle, WA 98103</div>
    </div>
  </section>

  <section class="card card-back">
    <div class="back-pattern" role="img" aria-label="Faint repeating brand pattern on dark teal background"></div>
    <div class="back-mark">KNEADWELL HAVEN</div>
  </section>
</div>
</body>
</html>
```